Qorvant Company Powerpoint Template

I would like to create a branded PowerPoint temple that my company can use for all presentations. our website is www.qorvant-example.com. The company is a software provider for the auto recycling industry (junk yards). Our customers use our software to pull, process, and deliver orders to auto body shops and mechanic shops.
Pages that would be helpful:
Title Page
Content slide
Content slide with image
Workflow/flowchart slide
Image only slide
Final slide

Target Market(s)

Automotive Recycling

Industry/Entity Type

Automotive recycling software

Font styles to use
Sans Serif

Colors
0054AA
0677BA
7BADD7
CADEEF
E8F1F8
FFF300
FFF600
FEFA6F
FFFEC7
FFFEE8

Requirements
Must have
• similarities in other branded items like our website. Title Page, Content slide, Content slide with image, Workflow/flowchart slide, Image only slide, Final slide
Nice to have
• Simple clean design would be preferential

```html
<!DOCTYPE html>
<html lang="en">
<head>
<meta charset="utf-8">
<title>Qorvant Presentation Template</title>
<link href="https://fonts.googleapis.com/css2?family=Ubuntu:wght@400;500;700&display=swap" rel="stylesheet">
<style>
:root{
  --blue:#0054AA; --mid:#0677BA; --sky:#7BADD7; --ice:#CADEEF; --mist:#E8F1F8;
  --yellow:#FFF300; --ink:#333; --grey:#777; --line:#ddd; --page:#e9e9ea;
  --photo-a:#8a7a66; --photo-b:#c9b497;
}
html,body{margin:0;padding:0}
body{width:690px;height:1200px;overflow:hidden;position:relative;
  background:linear-gradient(#dfe3e8 0,#e9e9ea 410px,var(--page) 100%);
  font-family:'Ubuntu',sans-serif}
.brand-mark{position:absolute;right:36px;top:26px;font-weight:700;font-size:30px;color:var(--blue);letter-spacing:.5px}
.slide{position:absolute;width:324px;height:182px;background:#fff}
.slide svg{display:block;width:100%;height:100%}
.slide--hero{left:65px;top:80px;width:560px;height:314px;box-shadow:0 6px 18px rgba(0,0,0,.18)}
.col-a{left:16px}.col-b{left:350px}
.row-1{top:423px}.row-2{top:616px}.row-3{top:809px}.row-4{top:1002px}
svg text{font-family:'Ubuntu',sans-serif}
.t-logo{font-weight:700;font-size:34px}
.t-title{font-weight:700;font-size:28px}
.t-sub{font-size:10px}
.t-small{font-size:7px}
.t-tiny{font-size:5px}
.t-head{font-weight:500;font-size:23px;fill:var(--blue)}
.t-subhead{font-size:8px;fill:#555}
.t-body{font-size:7.3px;fill:#444}
.t-item{font-size:15px;fill:#444}
.t-num{font-size:15px;fill:#bbb}
.t-foot{font-size:5.5px;fill:#222}
.t-footnum{font-size:5.5px;fill:var(--mid)}
.t-foot-brand{font-weight:700;font-size:13px;fill:var(--blue)}
.t-flow-h{font-size:9px;fill:#555;text-anchor:middle}
.t-flow-b{font-size:5.5px;fill:#777;text-anchor:middle}
</style>
</head>
<body>

<div class="brand-mark">Qorvant</div>

<!-- Hero: title slide, light -->
<div class="slide slide--hero">
<svg viewBox="0 0 683 383">
  <defs><linearGradient id="ph1" x1="0" y1="0" x2="1" y2="1"><stop offset="0" stop-color="var(--photo-b)"/><stop offset="1" stop-color="var(--photo-a)"/></linearGradient></defs>
  <rect width="683" height="383" fill="#fff"/>
  <path d="M228,0H683V383H370L445,262Q462,236 445,210Z" fill="url(#ph1)" role="img" aria-label="Warehouse worker on a lift among shelves of parts"/>
  <path d="M228,0H470L330,110Z" fill="var(--mid)" opacity=".8"/>
  <path d="M247,383L328,305Q340,292 352,305L435,383Z" fill="var(--blue)"/>
  <text x="40" y="95" class="t-logo" fill="var(--blue)">Qorvant</text>
  <text x="40" y="178" class="t-title" fill="var(--mid)">Presentation</text>
  <text x="40" y="212" class="t-title" fill="var(--mid)">Title Goes Here!</text>
  <rect x="40" y="230" width="70" height="3" fill="var(--yellow)"/>
  <text x="40" y="257" class="t-sub" fill="#555">Transforming Automotive Recycling</text>
  <rect x="40" y="302" width="135" height="18" rx="2" fill="var(--blue)"/>
  <text x="107" y="314" class="t-small" fill="#fff" text-anchor="middle">December 4, 2022</text>
  <text x="341" y="358" class="t-small" fill="#fff" text-anchor="middle">www.qorvant-example.com</text>
  <text x="341" y="368" class="t-tiny" fill="#fff" text-anchor="middle">©2020 by Qorvant.</text>
</svg>
</div>

<!-- Title slide, light -->
<div class="slide col-a row-1">
<svg viewBox="0 0 683 383">
  <defs><linearGradient id="ph2" x1="0" y1="0" x2="1" y2="1"><stop offset="0" stop-color="var(--photo-b)"/><stop offset="1" stop-color="var(--photo-a)"/></linearGradient></defs>
  <rect width="683" height="383" fill="#fff"/>
  <path d="M228,0H683V383H370L445,262Q462,236 445,210Z" fill="url(#ph2)" role="img" aria-label="Warehouse worker on a lift among shelves of parts"/>
  <path d="M228,0H470L330,110Z" fill="var(--mid)" opacity=".8"/>
  <path d="M247,383L328,305Q340,292 352,305L435,383Z" fill="var(--blue)"/>
  <text x="40" y="95" class="t-logo" fill="var(--blue)">Qorvant</text>
  <text x="40" y="178" class="t-title" fill="var(--mid)">Presentation</text>
  <text x="40" y="212" class="t-title" fill="var(--mid)">Title Goes Here!</text>
  <rect x="40" y="230" width="70" height="3" fill="var(--yellow)"/>
  <text x="40" y="257" class="t-sub" fill="#555">Transforming Automotive Recycling</text>
  <rect x="40" y="302" width="135" height="18" rx="2" fill="var(--blue)"/>
  <text x="107" y="314" class="t-small" fill="#fff" text-anchor="middle">December 4, 2022</text>
  <text x="341" y="358" class="t-small" fill="#fff" text-anchor="middle">www.qorvant-example.com</text>
  <text x="341" y="368" class="t-tiny" fill="#fff" text-anchor="middle">©2020 by Qorvant.</text>
</svg>
</div>

<!-- Title slide, dark -->
<div class="slide col-b row-1">
<svg viewBox="0 0 683 383">
  <defs><linearGradient id="ph3" x1="0" y1="0" x2="1" y2="1"><stop offset="0" stop-color="#9a9791"/><stop offset="1" stop-color="#5e5a55"/></linearGradient></defs>
  <rect width="683" height="383" fill="var(--blue)"/>
  <path d="M350,0H683V383H370L445,262Q462,236 445,210L350,120Z" fill="url(#ph3)" role="img" aria-label="Technician scanning an engine part with a tablet"/>
  <path d="M260,0H470L360,120Z" fill="var(--mid)" opacity=".8"/>
  <path d="M247,383L328,305Q340,292 352,305L435,383Z" fill="var(--sky)"/>
  <text x="40" y="95" class="t-logo" fill="#fff">Qorvant</text>
  <text x="40" y="178" class="t-title" fill="#fff">Presentation</text>
  <text x="40" y="212" class="t-title" fill="#fff">Title Goes Here!</text>
  <rect x="40" y="230" width="70" height="3" fill="var(--yellow)"/>
  <text x="40" y="257" class="t-sub" fill="#fff">Transforming Automotive Recycling</text>
  <rect x="40" y="302" width="135" height="18" rx="2" fill="var(--sky)"/>
  <text x="107" y="314" class="t-small" fill="#fff" text-anchor="middle">December 4, 2022</text>
  <text x="341" y="358" class="t-small" fill="#fff" text-anchor="middle">www.qorvant-example.com</text>
  <text x="341" y="368" class="t-tiny" fill="#fff" text-anchor="middle">©2020 by Qorvant.</text>
</svg>
</div>

<!-- Content list slide -->
<div class="slide col-a row-2">
<svg viewBox="0 0 683 383">
  <text x="175" y="205" font-weight="700" font-size="46" fill="var(--blue)" text-anchor="middle">Qorvant</text>
  <text x="364" y="75" class="t-head">Content</text>
  <rect x="364" y="85" width="44" height="3" fill="var(--yellow)"/>
  <g>
    <text x="364" y="145" class="t-num">01</text><text x="406" y="145" class="t-item">Title Goes Here</text>
    <line x1="356" y1="157" x2="610" y2="157" stroke="var(--line)"/>
    <text x="364" y="185" class="t-num">02</text><text x="406" y="185" class="t-item">Title Goes Here</text>
    <line x1="356" y1="197" x2="610" y2="197" stroke="var(--line)"/>
    <text x="364" y="225" class="t-num">03</text><text x="406" y="225" class="t-item">Title Goes Here</text>
    <line x1="356" y1="237" x2="610" y2="237" stroke="var(--line)"/>
    <text x="364" y="265" class="t-num">04</text><text x="406" y="265" class="t-item">Title Goes Here</text>
    <line x1="356" y1="277" x2="610" y2="277" stroke="var(--line)"/>
    <text x="364" y="305" class="t-num">05</text><text x="406" y="305" class="t-item">Title Goes Here</text>
  </g>
  <text x="18" y="364" class="t-foot-brand">Qorvant QC</text>
  <text x="645" y="364" class="t-foot" text-anchor="end">WWW.QORVANT-EXAMPLE.COM | ©2020 BY QORVANT. |</text>
  <text x="660" y="364" class="t-footnum">3</text>
</svg>
</div>

<!-- Text content slide -->
<div class="slide col-b row-2">
<svg viewBox="0 0 683 383">
  <text x="40" y="62" class="t-head">Heading Goes Here</text>
  <rect x="40" y="71" width="44" height="3" fill="var(--yellow)"/>
  <text x="40" y="95" class="t-subhead">Sub-Heading Goes Here</text>
  <g class="t-body">
    <text x="40" y="132">Lorem ipsum dolor sit amet, consectetur adipiscing elit. Vivamus eu dui ex. Curabitur dapibus dignissim dui, in molestie metus feugiat</text>
    <text x="40" y="142">sed. Praesent aliquet lorem ex, eu dapibus odio varius at. Duis eget tellus porta, consequat lacus vitae, venenatis dolor. Nulla facilisi.</text>
    <text x="40" y="152">In et sollicitudin lacus. Donec risus orci, gravida sit amet risus vehicula, aliquet pretium sapien. Nullam sit amet magna non ex</text>
    <text x="40" y="162">bibendum mollis. Nunc vel neque eu augue dignissim congue ut vitae magna. Phasellus eget commodo arcu. Nunc vitae semper dui.</text>
    <text x="40" y="172">Integer venenatis, tellus sit amet interdum pretium, erat neque rhoncus turpis, a aliquam augue ligula eget erat. Nunc placerat.</text>
    <text x="40" y="182">Pellentesque habitant morbi tristique senectus et netus et malesuada fames ac turpis egestas.</text>
    <text x="40" y="200">Lorem ipsum dolor sit amet, consectetur adipiscing elit. Vivamus eu dui ex. Curabitur dapibus dignissim dui, in molestie metus feugiat</text>
    <text x="40" y="210">sed. Praesent aliquet lorem ex, eu dapibus odio varius at. Duis eget tellus porta, consequat lacus vitae, venenatis dolor. Nulla facilisi.</text>
    <text x="40" y="220">In et sollicitudin lacus.</text>
    <text x="40" y="238">Donec risus orci, gravida sit amet risus vehicula, aliquet pretium sapien. Nullam sit amet magna non ex bibendum mollis. Nunc vel neque</text>
    <text x="40" y="248">eu augue dignissim congue ut vitae magna. Phasellus eget commodo arcu. Nunc vitae semper dui. Integer venenatis, tellus sit amet</text>
    <text x="40" y="258">interdum pretium, erat neque rhoncus turpis, a aliquam augue ligula eget erat. Nunc placerat, arcu nec mattis fermentum, nisi mauris</text>
    <text x="40" y="268">convallis nunc, ut luctus nunc nisl id ex. Nam semper tristique mauris, et vestibulum leo fringilla vel. Nulla id augue eleifend, egestas</text>
    <text x="40" y="278">ligula et, consequat massa. Pellentesque habitant morbi tristique senectus et netus et malesuada fames ac turpis egestas.</text>
  </g>
  <text x="18" y="364" class="t-foot-brand">Qorvant QC</text>
  <text x="645" y="364" class="t-foot" text-anchor="end">WWW.QORVANT-EXAMPLE.COM | ©2020 BY QORVANT. |</text>
  <text x="660" y="364" class="t-footnum">4</text>
</svg>
</div>

<!-- Content with image slide -->
<div class="slide col-a row-3">
<svg viewBox="0 0 683 383">
  <defs><linearGradient id="ph4" x1="0" y1="0" x2="1" y2="1"><stop offset="0" stop-color="var(--photo-b)"/><stop offset="1" stop-color="var(--photo-a)"/></linearGradient></defs>
  <text x="40" y="62" class="t-head">Heading Goes Here</text>
  <rect x="40" y="71" width="44" height="3" fill="var(--yellow)"/>
  <text x="40" y="95" class="t-subhead">Sub-Heading Goes Here</text>
  <g class="t-body">
    <text x="40" y="132">Lorem ipsum dolor sit amet, consectetur adipiscing elit. Vivamus eu</text>
    <text x="40" y="142">dui ex. Curabitur dapibus dignissim dui, in molestie metus feugiat sed.</text>
    <text x="40" y="152">Praesent aliquet lorem ex, eu dapibus odio varius at. Duis eget tellus</text>
    <text x="40" y="162">porta, consequat lacus vitae, venenatis dolor.</text>
    <text x="40" y="180">Nulla facilisi. In et sollicitudin lacus. Donec risus orci, gravida sit amet</text>
    <text x="40" y="190">risus vehicula, aliquet pretium sapien. Nullam sit amet magna non ex</text>
    <text x="40" y="200">bibendum mollis.</text>
    <text x="40" y="218">Nunc vel neque eu augue dignissim congue ut vitae magna. Phasellus</text>
    <text x="40" y="228">eget commodo arcu. Nunc vitae semper dui. Integer venenatis, tellus</text>
    <text x="40" y="238">sit amet interdum pretium, erat neque rhoncus turpis, a aliquam</text>
    <text x="40" y="248">augue ligula eget erat.</text>
    <text x="40" y="266">Nunc placerat, arcu nec mattis fermentum, nisi mauris convallis nunc,</text>
    <text x="40" y="276">ut luctus nunc nisl id ex. Nam semper tristique mauris, et vestibulum</text>
    <text x="40" y="286">leo fringilla vel. Nulla id augue eleifend, egestas ligula et, consequat</text>
    <text x="40" y="296">massa. Pellentesque habitant morbi tristique senectus et netus et</text>
    <text x="40" y="306">malesuada fames ac turpis egestas.</text>
  </g>
  <rect x="370" y="35" width="278" height="285" fill="url(#ph4)" role="img" aria-label="Warehouse aisle with a worker on a lift"/>
  <text x="18" y="364" class="t-foot-brand">Qorvant QC</text>
  <text x="645" y="364" class="t-foot" text-anchor="end">WWW.QORVANT-EXAMPLE.COM | ©2020 BY QORVANT. |</text>
  <text x="660" y="364" class="t-footnum">5</text>
</svg>
</div>

<!-- Workflow slide -->
<div class="slide col-b row-3">
<svg viewBox="0 0 683 383">
  <text x="40" y="62" class="t-head">Workflow / Flowchart Slide</text>
  <rect x="40" y="71" width="44" height="3" fill="var(--yellow)"/>
  <g fill="none" stroke-width="6">
    <path d="M33,210 A64,64 0 0 1 158,195" stroke="var(--blue)"/>
    <path d="M158,225 A64,64 0 0 0 280,225" stroke="var(--sky)"/>
    <path d="M280,195 A64,64 0 0 1 402,195" stroke="var(--blue)"/>
    <path d="M402,225 A64,64 0 0 0 524,225" stroke="var(--sky)"/>
    <path d="M524,195 A64,64 0 0 1 650,210" stroke="var(--blue)"/>
  </g>
  <g>
    <path d="M152,202h12l-6,9z" fill="var(--blue)"/>
    <path d="M274,218h12l-6,-9z" fill="var(--sky)"/>
    <path d="M396,202h12l-6,9z" fill="var(--blue)"/>
    <path d="M518,218h12l-6,-9z" fill="var(--sky)"/>
  </g>
  <circle cx="97" cy="210" r="40" fill="var(--mid)"/>
  <circle cx="219" cy="210" r="40" fill="var(--sky)"/>
  <circle cx="341" cy="210" r="40" fill="var(--mid)"/>
  <circle cx="463" cy="210" r="40" fill="var(--sky)"/>
  <circle cx="585" cy="210" r="40" fill="var(--mid)"/>
  <g fill="#fff">
    <path d="M97,192a12,12 0 0 0-7,22v6h14v-6a12,12 0 0 0-7-22z"/><rect x="91" y="222" width="12" height="3"/><rect x="93" y="227" width="8" height="3"/>
    <circle cx="211" cy="203" r="5"/><circle cx="227" cy="203" r="5"/><circle cx="219" cy="200" r="6"/>
    <path d="M203,222q0-12 8-12h16q8,0 8,12z"/>
    <circle cx="337" cy="206" r="11" fill="none" stroke="#fff" stroke-width="4"/><path d="M344,214l10,10-4,4-10-10z"/>
    <circle cx="463" cy="210" r="13" fill="none" stroke="#fff" stroke-width="5" stroke-dasharray="5 3"/><circle cx="463" cy="210" r="6" fill="none" stroke="#fff" stroke-width="3"/>
    <rect x="573" y="214" width="6" height="10"/><rect x="581" y="208" width="6" height="16"/><rect x="589" y="202" width="6" height="22"/>
    <path d="M572,206l10-8 6,4 10-10" fill="none" stroke="#fff" stroke-width="2"/>
  </g>
  <g>
    <text x="219" y="115" class="t-flow-h">Heading</text>
    <text x="219" y="126" class="t-flow-b">Nunc vel neque eu augue</text>
    <text x="219" y="132" class="t-flow-b">dignissim congue ut vitae</text>
    <text x="219" y="138" class="t-flow-b">magna. Phasellus eget</text>
    <text x="219" y="144" class="t-flow-b">commodo arcu.</text>
    <text x="463" y="115" class="t-flow-h">Heading</text>
    <text x="463" y="126" class="t-flow-b">Nunc vel neque eu augue</text>
    <text x="463" y="132" class="t-flow-b">dignissim congue ut vitae</text>
    <text x="463" y="138" class="t-flow-b">magna. Phasellus eget</text>
    <text x="463" y="144" class="t-flow-b">commodo arcu.</text>
    <text x="97" y="272" class="t-flow-h">Heading</text>
    <text x="97" y="283" class="t-flow-b">Nunc vel neque eu augue</text>
    <text x="97" y="289" class="t-flow-b">dignissim congue ut vitae</text>
    <text x="97" y="295" class="t-flow-b">magna. Phasellus eget</text>
    <text x="97" y="301" class="t-flow-b">commodo arcu.</text>
    <text x="341" y="272" class="t-flow-h">Heading</text>
    <text x="341" y="283" class="t-flow-b">Nunc vel neque eu augue</text>
    <text x="341" y="289" class="t-flow-b">dignissim congue ut vitae</text>
    <text x="341" y="295" class="t-flow-b">magna. Phasellus eget</text>
    <text x="341" y="301" class="t-flow-b">commodo arcu.</text>
    <text x="585" y="272" class="t-flow-h">Heading</text>
    <text x="585" y="283" class="t-flow-b">Nunc vel neque eu augue</text>
    <text x="585" y="289" class="t-flow-b">dignissim congue ut vitae</text>
    <text x="585" y="295" class="t-flow-b">magna. Phasellus eget</text>
    <text x="585" y="301" class="t-flow-b">commodo arcu.</text>
  </g>
  <text x="18" y="364" class="t-foot-brand">Qorvant QC</text>
  <text x="645" y="364" class="t-foot" text-anchor="end">WWW.QORVANT-EXAMPLE.COM | ©2020 BY QORVANT. |</text>
  <text x="660" y="364" class="t-footnum">6</text>
</svg>
</div>

<!-- Image only slide -->
<div class="slide col-a row-4">
<svg viewBox="0 0 683 383">
  <defs><linearGradient id="ph5" x1="0" y1="0" x2="1" y2="1"><stop offset="0" stop-color="#a5a098"/><stop offset="1" stop-color="#5a5650"/></linearGradient></defs>
  <rect x="35" y="35" width="613" height="285" fill="url(#ph5)" role="img" aria-label="Technician checking an engine part with a tablet"/>
  <text x="18" y="364" class="t-foot-brand">Qorvant QC</text>
  <text x="645" y="364" class="t-foot" text-anchor="end">WWW.QORVANT-EXAMPLE.COM | ©2020 BY QORVANT. |</text>
  <text x="660" y="364" class="t-footnum">7</text>
</svg>
</div>

<!-- Closing slide -->
<div class="slide col-b row-4">
<svg viewBox="0 0 683 383">
  <defs><linearGradient id="ph6" x1="0" y1="0" x2="1" y2="1"><stop offset="0" stop-color="#1f5fae"/><stop offset="1" stop-color="#2a6db8"/></linearGradient></defs>
  <rect width="683" height="383" fill="url(#ph6)" role="img" aria-label="Warehouse shelving under a blue tint"/>
  <text x="68" y="138" class="t-logo" fill="#fff">Qorvant</text>
  <text x="68" y="190" font-weight="500" font-size="13" fill="#fff">Contact Us</text>
  <text x="68" y="210" class="t-body" fill="#fff" style="fill:#fff">450 Harbor Line Ave. Fairview OH 44000</text>
  <g fill="none" stroke="#fff" stroke-width="1.2">
    <path d="M70,233q2,6 8,8l2-2-3-2-1,1q-2-1-3-3l1-1-2-3z"/>
    <circle cx="74" cy="254" r="4.5"/><circle cx="74" cy="254" r="1.8"/>
    <circle cx="74" cy="274" r="5"/><path d="M69,274h10M74,269q-3,5 0,10q3-5 0-10"/>
  </g>
  <g class="t-body" style="fill:#fff">
    <text x="90" y="240" fill="#fff">555-010-0199</text>
    <text x="90" y="257" fill="#fff">Support@qorvant-example.com</text>
    <text x="90" y="277" fill="#fff">www.qorvant-example.com</text>
  </g>
  <text x="341" y="368" class="t-tiny" fill="#fff" text-anchor="middle">©2020 by Qorvant.</text>
</svg>
</div>

</body>
</html>
```